Bluegate Gatherings Web Design Layout (no HTML)

We require the layout only for a website.  No html or logo is required - just the layout.

A refreshed and revitalized website to coincide with the relaunch of our brand. We are looking for a clean simplistic design that is easy to use and presents relevant information effectively.
We are an events management company specializing in conferences.
Updates

Thank you for your design. We really like the imagery. Essentially we are after a home page design (one page) that incorporates the 3 main buttons (request a proposal, select a venue and specials) while providing the relevant information on our service via functionality similar to that on www.trelvasite.com ie using the large arrow to scroll over the relevant topic to receive information. We hope to finalise the contest in the next week and hope to consider your revised entry.

Thanks!

Target Market(s)

Australian corporate sector primarily Managing Directors or their assistants. Any business looking to hold a conference for up 500 delegates however we are primarily targeting the decision maker so need to ensure we are communicating on their terms.

Industry/Entity Type

Event

Requirements
Must have
• Incorporate the elements from the attached document however with complete creative license as to their layout. Our main competitors are pordamhosting.com.au, brimwellsummits.com.au both sites are bland and not user friendly.
Nice to have
• Colours red, silver and black. Note we are running a separate contest to refresh our logo.
• We like the functionality of trelvasite.com

```html
<!DOCTYPE html>
<html lang="en">
<head>
<meta charset="utf-8">
<title>Bluegate Gatherings – Conference Management</title>
<link href="https://fonts.googleapis.com/css2?family=Arimo:wght@400;700&family=Open+Sans:wght@400;600;700&display=swap" rel="stylesheet">
<style>
  :root {
    --red: #c8474a;
    --red-dark: #a8393c;
    --red-text: #c0393d;
    --nav: #4d5163;
    --nav-dark: #3b3e4d;
    --silver-light: #f4f4f4;
    --silver: #c9c9c9;
    --silver-dark: #a9a9a9;
    --ink: #1c1c1c;
    --white: #ffffff;
    --footer: #e1e2e6;
  }
  * { box-sizing: border-box; margin: 0; padding: 0; }
  html, body { width: 1200px; height: 1067px; overflow: hidden; background: var(--white); }
  body { position: relative; font-family: "Open Sans", Arial, sans-serif; color: var(--ink); }

  .header {
    position: absolute; left: 17px; top: 4px; width: 1162px; height: 169px;
    background: linear-gradient(180deg, #fafafa 0%, #e4e4e6 55%, #cfd0d3 100%);
    border: 1px solid #dcdcdc;
  }
  .brand { position: absolute; left: 24px; top: 64px; display: flex; align-items: center; gap: 12px; }
  .brand-mark { width: 22px; height: 22px; background: var(--red); }
  .brand-name { font-family: "Arimo", Arial, sans-serif; font-weight: 700; font-size: 30px; color: #4a4a4a; letter-spacing: -0.5px; }
  .team-photo {
    position: absolute; right: 0; top: 0; width: 458px; height: 167px;
    background: linear-gradient(90deg, rgba(230,230,232,0) 0%, #c9b7a8 25%, #e6e0da 55%, #9c8c80 100%);
  }

  .nav {
    position: absolute; left: 13px; top: 177px; width: 1167px; height: 43px;
    background: linear-gradient(180deg, #5c6074 0%, var(--nav) 50%, var(--nav-dark) 100%);
    display: flex; align-items: center; justify-content: center;
    font-family: "Arimo", Arial, sans-serif; font-size: 18.5px; color: var(--white);
  }
  .nav span { padding: 0 15px; }
  .nav .sep { padding: 0; }

  .topic-panel {
    position: absolute; left: 24px; top: 236px; width: 389px; height: 433px;
    background: var(--red); border: 4px solid var(--white);
    box-shadow: 0 1px 5px rgba(0,0,0,0.35); color: var(--white);
  }
  .topic-intro { position: absolute; left: 20px; top: 30px; width: 350px; font-size: 17.5px; line-height: 24.5px; text-align: justify; }
  .topic-goal { position: absolute; left: 20px; top: 174px; width: 350px; font-size: 17.5px; line-height: 24.5px; }
  .topic-list { list-style: none; position: absolute; left: 0; top: 232px; width: 100%; }
  .topic-list li { height: 49px; line-height: 49px; padding-left: 20px; font-size: 17.5px; }
  .topic-list li.is-active { font-weight: 600; color: var(--white); }
  .topic-arrow { position: absolute; left: 33px; top: 471px; width: 400px; height: 46px; }
  .topic-arrow-label { position: absolute; left: 47px; top: 471px; line-height: 46px; font-size: 17.5px; font-weight: 600; color: var(--white); }

  .info-panel {
    position: absolute; left: 433px; top: 236px; width: 455px; height: 435px;
    background: linear-gradient(180deg, #f2f2f2 0%, #dedede 60%, #bdbdbd 100%);
    border: 1px solid #c4c4c4; box-shadow: 0 1px 4px rgba(0,0,0,0.25);
    padding: 33px 22px 0 21px; font-size: 17.5px; line-height: 24.5px;
  }
  .info-panel ul { list-style: none; }
  .info-panel li::before { content: "• "; }
  .info-panel .info-close { margin-top: 24px; }
  .info-link { color: var(--red-text); font-weight: 700; text-decoration: underline; }

  .side-card {
    position: absolute; left: 907px; width: 272px;
    border: 4px solid var(--red); border-radius: 22px; background: var(--white);
    box-shadow: 0 1px 4px rgba(0,0,0,0.3);
  }
  .side-card h3 { position: absolute; left: 18px; top: 10px; font-family: "Arimo", Arial, sans-serif; font-size: 18.5px; font-weight: 700; color: var(--red-text); }
  .side-card p { position: absolute; left: 120px; top: 36px; width: 136px; font-size: 12px; line-height: 16.5px; }
  .side-art { position: absolute; left: 16px; top: 40px; width: 90px; height: 76px; }
  .card-venues { top: 236px; height: 141px; }
  .card-venues h3 { left: 20px; top: 9px; font-size: 17px; letter-spacing: -0.3px; }
  .card-venues p { top: 34px; left: 124px; width: 130px; font-size: 11.5px; line-height: 16px; }
  .card-venues .side-art { background: linear-gradient(160deg, #d8383c, #b52025); width: 96px; top: 38px; height: 80px; }
  .card-proposal { top: 396px; height: 151px; }
  .card-proposal p { top: 48px; }
  .card-proposal .side-art { background: radial-gradient(circle, #ffffff 0 45%, #c92b2f 48% 60%, #e8e8e8 63%); top: 46px; width: 80px; height: 80px; left: 20px; border-radius: 50%; }
  .card-offers { top: 567px; height: 150px; }
  .card-offers p { top: 44px; left: 100px; width: 150px; }
  .card-offers .side-art { background: linear-gradient(160deg, #f08a5f, #c7322f); left: 30px; top: 48px; width: 56px; height: 70px; border-radius: 8px; }

  .promo { position: absolute; left: 916px; width: 252px; border-radius: 3px; }
  .promo-flight { top: 729px; height: 112px; background: linear-gradient(135deg, #ffffff 0%, #d9e3ee 45%, #7d93ad 100%); border: 1px solid #c9c9c9; }
  .promo-flight .title { position: absolute; left: 10px; top: 6px; font-family: "Arimo", Arial, sans-serif; font-size: 19px; font-weight: 700; color: #d2252b; line-height: 22px; }
  .promo-flight .price { position: absolute; left: 10px; top: 54px; font-family: "Arimo", Arial, sans-serif; font-size: 30px; font-weight: 700; color: #333; }
  .promo-flight .price small { font-size: 11px; font-weight: 400; }
  .promo-flight .more { position: absolute; left: 0; bottom: 0; width: 100%; height: 20px; background: #c9262b; color: var(--white); font-size: 11px; font-weight: 700; line-height: 20px; padding-left: 10px; }
  .promo-win { top: 859px; height: 72px; background: linear-gradient(180deg, #e0363a 0%, #c21f24 55%, #a8181c 100%); color: var(--white); font-family: "Arimo", Arial, sans-serif; }
  .promo-win .line { position: absolute; left: 14px; top: 6px; font-size: 15.5px; font-weight: 700; line-height: 21px; letter-spacing: -0.3px; }
  .promo-win .line b { font-size: 20px; }
  .promo-go { position: absolute; right: 6px; bottom: 4px; width: 44px; height: 18px; border-radius: 9px; background: linear-gradient(180deg, #f2f2f2, #9d9d9d); color: #333; font-size: 12px; font-weight: 700; text-align: center; line-height: 18px; }
  .promo-currency { top: 949px; height: 38px; background: linear-gradient(180deg, #6d9ad8 0%, #2f66b8 55%, #1d4d98 100%); color: var(--white); font-family: "Arimo", Arial, sans-serif; }
  .promo-currency .line { position: absolute; left: 38px; top: 8px; font-size: 17.5px; font-weight: 700; }
  .promo-currency .promo-go { bottom: 6px; }
  .promo-currency .icon { position: absolute; left: 8px; top: 8px; width: 24px; height: 22px; background: #dfe9f6; border-radius: 3px; }

  .summary { position: absolute; left: 47px; top: 686px; width: 520px; font-size: 18px; line-height: 25px; }
  .summary .lead { margin-top: 2px; }
  .feature-bar {
    position: absolute; left: 25px; top: 819px; width: 602px; height: 60px;
    background: linear-gradient(180deg, #d3383b 0%, #c8373a 45%, #f0dada 100%);
    border: 1px solid #b9b9b9; color: var(--white);
    font-family: "Arimo", Arial, sans-serif; font-size: 27px; line-height: 56px; padding-left: 33px;
  }
  .feature-item { position: absolute; left: 59px; font-family: "Arimo", Arial, sans-serif; font-weight: 700; font-size: 28px; color: var(--red-text); }

  .footer {
    position: absolute; left: 13px; top: 996px; width: 1167px; height: 71px;
    background: var(--footer); text-align: center;
    font-family: "Arimo", Arial, sans-serif; font-size: 16px; line-height: 38px; padding-top: 16px;
  }
</style>
</head>
<body>
  <header class="header">
    <div class="brand">
      <span class="brand-mark"></span>
      <span class="brand-name">Bluegate Gatherings</span>
    </div>
    <div class="team-photo" role="img" aria-label="Photo of three smiling event consultants, one wearing a headset"></div>
  </header>

  <nav class="nav">
    <span>Home</span><span class="sep">|</span>
    <span>Services</span><span class="sep">|</span>
    <span>Finance Option</span><span class="sep">|</span>
    <span>Registration</span><span class="sep">|</span>
    <span>System</span><span class="sep">|</span>
    <span>Venues</span><span class="sep">|</span>
    <span>Clients</span><span class="sep">|</span>
    <span>Register</span><span class="sep">|</span>
    <span>Contact Us</span>
  </nav>

  <section class="topic-panel">
    <p class="topic-intro">Bluegate Gatherings’ professional conference team specialises in solutions. We work closely with a core group of clients to ensure desired outcomes, on time and in budget.</p>
    <p class="topic-goal">Our goal is to make sure your conference is;</p>
    <ul class="topic-list">
      <li class="is-active">&nbsp;</li>
      <li>Expertly Managed and Hassle Free</li>
      <li>Outcome focused</li>
      <li>Well Attended</li>
    </ul>
  </section>

  <section class="info-panel">
    <p>We offer a complete range of finance packages including;</p>
    <ul>
      <li>total conference underwriting</li>
      <li>online delegate payment gateway</li>
      <li>substantially discounted rooming rates</li>
      <li>no upfront costs</li>
      <li>zero management fees</li>
      <li>free venue sourcing</li>
      <li>free delegate booking management</li>
    </ul>
    <p class="info-close">Minimise your costs and free your cash flow to focus on your core business functions. We’ll ensure maximum return from your conference budget. <span class="info-link">Learn how?</span></p>
  </section>

  <svg class="topic-arrow" viewBox="0 0 400 46" aria-hidden="true">
    <defs>
      <linearGradient id="arrowFill" x1="0" y1="0" x2="0" y2="1">
        <stop offset="0" stop-color="#b8b8b8"/>
        <stop offset="1" stop-color="#8f8f8f"/>
      </linearGradient>
    </defs>
    <polygon points="0,0 377,0 400,23 377,46 0,46" fill="url(#arrowFill)"/>
  </svg>
  <span class="topic-arrow-label">Cost Effective</span>

  <aside class="side-card card-venues">
    <h3>Browse Conference Venues</h3>
    <div class="side-art" role="img" aria-label="Red map of Australia showing states"></div>
    <p>Not sure where to start? We have over 60 properties to choose from both domestically and international.</p>
  </aside>
  <aside class="side-card card-proposal">
    <h3>Request a Proposal</h3>
    <div class="side-art" role="img" aria-label="Red alarm clock illustration"></div>
    <p>Prefer us to do the leg work? We can prepare and return a proposal within 24 hours of receipt.</p>
  </aside>
  <aside class="side-card card-offers">
    <h3>Special Offers</h3>
    <div class="side-art" role="img" aria-label="Glossy orange dollar sign illustration"></div>
    <p>Always looking for a bargain? Save money with one of our special offers available for a limited time.</p>
  </aside>

  <div class="promo promo-flight" role="img" aria-label="Domestic flight sale banner with a jet in a blue sky">
    <div class="title">Domestic flight<br>sale on now!</div>
    <div class="price"><small>From </small>$28<small>* One way</small></div>
    <div class="more">More Details Here &gt;&gt;</div>
  </div>
  <div class="promo promo-win">
    <div class="line"><b>WIN</b> tickets to L.A.<br>Bali or Sola Vey in concert</div>
    <span class="promo-go">go »</span>
  </div>
  <div class="promo promo-currency">
    <span class="icon"></span>
    <div class="line">Convert Currency</div>
    <span class="promo-go">go »</span>
  </div>

  <section class="summary">
    <p>Bluegate Gatherings’ professional conference team specialises in solutions. We work closely with a core group of clients to ensure desired outcomes, on time and in budget.</p>
    <p class="lead">We’ll ensure your conference is;</p>
  </section>
  <div class="feature-bar">Cost Effective</div>
  <div class="feature-item" style="top:887px;">Expertly managed and hassle free</div>
  <div class="feature-item" style="top:937px;">Impressive</div>

  <footer class="footer">Ph: 1300 555 014. P.O. Box 4471, Carrow Bay NSW 2099. Bluegate Gatherings. All Rights Reserved. 2009</footer>
</body>
</html>
```